Job advertisement

A graphic job advertisement. It's supposed to be slightly different from the normal ads. Eye-catcher and later the text for the job description.

```html
<!DOCTYPE html>
<html lang="de">
<head>
<meta charset="utf-8">
<title>Stellenanzeige – elektro brandauer</title>
<link rel="stylesheet" href="https://fonts.googleapis.com/css2?family=Bitter:wght@400;700&family=Quicksand:wght@500&display=swap">
<style>
  :root {
    --brand-red: #e2001a;
    --text-dark: #3a3a3a;
    --logo-grey: #5f6366;
    --badge-blue: #12b5e8;
    --badge-text: #ffffff;
    --bg-white: #ffffff;
    --bg-tint: #e9f0fb;
  }
  * { margin: 0; padding: 0; box-sizing: border-box; }
  html, body { width: 1053px; height: 1200px; overflow: hidden; }
  body {
    position: relative;
    background: linear-gradient(90deg, var(--bg-white) 55%, var(--bg-tint) 100%);
    font-family: "Bitter", Georgia, serif;
    color: var(--text-dark);
  }
  .ad { position: relative; width: 1053px; height: 1200px; overflow: hidden; }

  .bulb-artwork {
    position: absolute; left: 0; top: 0; width: 760px; height: 1200px;
    background:
      radial-gradient(ellipse 300px 380px at 270px 380px, rgba(255,236,80,.95), rgba(255,190,40,.6) 55%, transparent 80%),
      radial-gradient(ellipse 200px 260px at 470px 330px, rgba(255,110,190,.55), transparent 75%),
      radial-gradient(ellipse 380px 300px at 250px 170px, rgba(240,60,40,.6), transparent 75%),
      radial-gradient(ellipse 230px 260px at 220px 860px, rgba(230,50,50,.35), transparent 75%),
      radial-gradient(ellipse 260px 170px at 160px 1110px, rgba(40,170,240,.85), rgba(40,80,200,.4) 60%, transparent 85%);
  }

  .badge {
    position: absolute;
    display: flex; align-items: center; justify-content: center;
    height: 57px;
    background: var(--badge-blue);
    color: var(--badge-text);
    border: 2px solid #ffffff;
    border-radius: 12px;
    font-family: "Quicksand", "Century Gothic", sans-serif;
    font-weight: 500;
    font-size: 32px;
    letter-spacing: 1px;
    box-shadow: 0 2px 4px rgba(0,0,0,.12);
  }
  .badge--watt     { left: 166px; top: 131px; width: 137px; }
  .badge--strom    { left: 368px; top: 181px; width: 158px; }
  .badge--volt     { left: 200px; top: 268px; width: 137px; }
  .badge--ampere   { left: 208px; top: 398px; width: 179px; }
  .badge--ohm      { left: 463px; top: 391px; width: 126px; }
  .badge--spannung { left: 331px; top: 526px; width: 234px; }
  .badge--leistung { left: 269px; top: 690px; width: 231px; }

  .brand {
    position: absolute; right: 56px; top: 150px;
    display: flex; align-items: center; gap: 14px;
  }
  .brand__mark { width: 22px; height: 22px; border-radius: 50%; background: var(--brand-red); }
  .brand__name {
    font-family: "Bitter", Georgia, serif; font-weight: 400;
    color: var(--logo-grey); font-size: 38px; line-height: 1;
  }

  .job {
    position: absolute; right: 56px; top: 418px; width: 360px;
    text-align: right;
  }
  .job__title {
    color: var(--brand-red); font-weight: 400; font-size: 33px; line-height: 1.2;
    margin-bottom: 12px;
  }
  .job__text { font-size: 20.5px; line-height: 34px; margin-bottom: 8px; }

  .contact {
    position: absolute; right: 56px; top: 982px; text-align: right;
  }
  .contact__line { font-size: 26px; line-height: 40px; }
  .contact__email {
    color: var(--brand-red); font-weight: 700; font-size: 28px; line-height: 46px;
  }
</style>
</head>
<body>
<main class="ad">
  <div class="bulb-artwork" role="img" aria-label="Farbige, polygonale Glühbirne aus Linien und Flächen in Gelb, Orange, Rot, Pink und Blau"></div>

  <span class="badge badge--watt">WATT</span>
  <span class="badge badge--strom">STROM</span>
  <span class="badge badge--volt">VOLT</span>
  <span class="badge badge--ampere">AMPERE</span>
  <span class="badge badge--ohm">OHM</span>
  <span class="badge badge--spannung">SPANNUNG</span>
  <span class="badge badge--leistung">LEISTUNG</span>

  <div class="brand">
    <span class="brand__mark"></span>
    <span class="brand__name">elektro brandauer</span>
  </div>

  <section class="job">
    <h1 class="job__title">Stellenazeige</h1>
    <p class="job__text">Lorem ipsum dolor sit amet, consectetuer adipiscing elit, sed diam nonummy nibh euismod tincidunt ut laoreet dolore magna.</p>
    <p class="job__text">Lorem ipsum dolor sit amet, consectetuer adipiscing elit, sed diam nonummy.</p>
  </section>

  <section class="contact">
    <p class="contact__line">Wir Stellen Ein !</p>
    <p class="contact__line">siehe Anhang</p>
    <p class="contact__email">personal@elektro-brandauer.de</p>
  </section>
</main>
</body>
</html>
```